Postcard designed to acquire new customers

Need a postcard style AD to place in dentist offices and other professionals to promote our tax saving system. We will place these in dentists offices, orthodontist, optometrist, physiotherapist and all sorts of medical/dental offices. The card should highlight how they can save taxes by using our software. Our website has good information on it, and I'll include the advertising PDF that our software company produces. Our logo is a little out-dated and I've included the bonus of the winner re-making the logo so its better than it currently is.
Updates

I don't need to have any space allocated for a stamp and address. We are using this to place in offices and are for advertising purposes, not mailing. Thanks!

Reason: My apologies for not providing feedback yet, I've lost several days due to some illness and am finally back at work. I'll be going through designs today and would like the extra few days to work with many of you to create a great design. Thank you for your patience! Doyle

Reason: Again, my apologies for the delay. I will be in contact with designers this week. Thank you,

Target Market(s)

Small Business Owners in Canada

Industry/Entity Type

Health Insurance

Logo Text

Save Time, Save Money

Font styles to use
Other font styles liked:
• Easy to Read Font's

Colors

Designer to choose colors to be used in the design.

Requirements
Must have
• Must have a call to action on the postcard to sell the service. We need people to have their attention caught. A call to action could be, "You're spending too much on taxes! That's what they'll say if your business doesn't have a 789 Brookvale Outlay Plan..."
• See the PDF for other catch phrases or key information on what a Health Spending Account is. Many people don't know so I'd like to see 3-4 bullet points on the front of the postcard on what a health spending account is. See the attached PDF for that information and simplifying the information to short bullet points would be best. Here are my thoughts:
• Who should have a 789 Brookvale Outlay Plan?
• - Every business owner who is incorporated should have one.
• - Write off 100% of this QTB approved this method.
• - It is the most tax effective way to run dental, health, vision and other expenses through your company.
• - Easy to use APP for your phone, 2-day turnaround time for claims
• If you aren't using this, you're throwing tax dollars away!
• The back of the postcard would include 2 things. First, an example of the taxes you can save, and second - the different information they can send us so we can setup your account.
• First is the example of how this saves you money. Assuming a 38% personal tax rate. You will need to earn $1.62 of gross income, pay $0.62 of personal tax, which leaves you with $1.00 of after tax money to use for your personal expenses.
• The example of using a 789 Brookvale Outlay Plan, or doing nothing would need the following information.
• Comparison
• $5,000 of medical, dental, vision expenses
• Do Nothing 789 Brookvale Outlay Plan
• $8,100 – Total Cost $5,525 – Total Cost
• $3,100 – Income Tax $500 fee & $25 GST
• $5,000 – Money needed for medical, dental, vision, etc. $5,000 – Money needed for medical, dental, vision, etc.
• SAVINGS is $2,575
• Assuming a company incorporated in Alberta and a one time setup fee of $275 has not been included in the comparison.
• Information to send us to setup your account is:
• - Names and birth dates of you and your dependents
• - Contact information for you and your business (if different) Address, email, phone numbers
• - We will contact you about how to setup the app, your banking details and some other items.
• - Setup fee is a one-time payment of $275
Nice to have
• I'd like the front of the postcard to not be very busy with the background or graphics, etc. I want the call to action to be very obvious so they want to read the bullet points and look at the back of the postcard for more information.

```html
<!DOCTYPE html>
<html lang="en">
<head>
<meta charset="utf-8">
<title>789 Brookvale Outlay Plan – Postcard</title>
<link rel="stylesheet" href="https://fonts.googleapis.com/css2?family=Oswald:wght@400;500;600&family=Roboto+Condensed:ital,wght@0,400;0,700;1,400;1,700&family=Montserrat:wght@600;700&display=swap">
<style>
  :root {
    --bg: #2b2b2d;
    --blue: #1d64b4;
    --green: #33a853;
    --orange: #f0a01e;
    --ice: #9fd3f5;
    --ink: #222428;
    --grey-text: #4a4d52;
    --white: #ffffff;
  }
  * { box-sizing: border-box; margin: 0; padding: 0; }
  html, body { width: 1200px; height: 1000px; overflow: hidden; }
  body {
    background: var(--bg);
    display: flex; flex-direction: column; align-items: center; justify-content: center;
    gap: 20px;
    font-family: "Roboto Condensed", sans-serif;
  }
  .card {
    width: 740px; height: 476px; position: relative; overflow: hidden;
    box-shadow: 0 6px 18px rgba(0,0,0,.45);
  }

  /* ---------- front ---------- */
  .front { background: var(--blue); }
  .front-top {
    position: absolute; left: 0; top: 0; right: 0; height: 158px;
    background: linear-gradient(#ffffff 0%, #eeeeee 60%, #d9d9d9 100%);
    border-bottom: 7px solid var(--green);
    display: flex; align-items: center; justify-content: center;
  }
  .brand { display: flex; align-items: center; gap: 14px; }
  .brand-dot { width: 32px; height: 32px; border-radius: 50%; background: var(--blue); flex: none; }
  .brand-name {
    font-family: "Oswald", sans-serif; font-weight: 500; font-size: 40px;
    color: var(--ink); letter-spacing: 2px; text-transform: uppercase; white-space: nowrap;
  }
  .headline {
    position: absolute; left: 0; right: 0; top: 170px;
    text-align: center; color: var(--white); white-space: nowrap;
    font-family: "Oswald", sans-serif; font-weight: 500;
    font-size: 42px; line-height: 1;
  }
  .tagline-box {
    position: absolute; left: 50%; top: 224px; transform: translateX(-50%);
    background: #0b0b0b; border: 2px solid #d8d8d8; border-radius: 5px;
    color: var(--white); white-space: nowrap;
    font-size: 17px; line-height: 1; padding: 5px 10px;
  }
  .tagline-box em { font-style: normal; color: var(--ice); }
  .who {
    position: absolute; left: 0; right: 0; top: 266px;
    text-align: center; color: var(--ice); white-space: nowrap;
    font-family: "Montserrat", sans-serif; font-weight: 700; font-size: 19px;
  }
  .points {
    position: absolute; left: 20px; right: 20px; top: 306px;
    display: flex; justify-content: center; align-items: flex-start;
  }
  .point {
    color: var(--white); font-size: 11.5px; line-height: 1.3; text-align: center;
    padding: 2px 12px; border-right: 2px solid rgba(10,30,70,.55);
  }
  .point:last-child { border-right: none; }
  .point:nth-child(1) { width: 158px; }
  .point:nth-child(2) { width: 130px; }
  .point:nth-child(3) { width: 220px; }
  .point:nth-child(4) { width: 180px; }
  .url-bar {
    position: absolute; left: 0; right: 0; top: 414px; height: 32px;
    background: linear-gradient(90deg, rgba(51,168,83,0) 0%, var(--green) 22%, var(--green) 100%);
    display: flex; align-items: center; justify-content: center;
    color: var(--white); font-family: "Montserrat", sans-serif; font-weight: 700; font-size: 18px;
  }

  /* ---------- back ---------- */
  .back { display: flex; background: var(--white); }
  .example {
    width: 57%; background: var(--blue); color: var(--white);
    border-right: 6px solid var(--green);
    padding: 16px 22px 14px 24px; font-size: 13.5px; line-height: 1.22;
  }
  .example p { margin-bottom: 11px; }
  .example .lead { font-style: italic; }
  .example .lead.strong { font-weight: 700; }
  .example .sub { margin-bottom: 1px; }
  .example ul { list-style: none; margin-bottom: 11px; }
  .example li { padding-left: 11px; position: relative; }
  .example li::before {
    content: ""; position: absolute; left: 0; top: 6px; width: 5px; height: 5px; background: var(--ice);
  }
  .example li.plain::before { display: none; }
  .amt { color: var(--orange); }
  .setup {
    flex: 1; padding: 18px 18px 20px 18px; display: flex; flex-direction: column;
  }
  .setup h3 {
    color: var(--blue); font-style: italic; font-weight: 700; font-size: 13.5px; margin-bottom: 4px;
  }
  .setup ul { list-style: none; color: var(--grey-text); font-size: 13px; line-height: 1.3; }
  .setup li { padding-left: 11px; position: relative; margin-bottom: 24px; }
  .setup li::before {
    content: ""; position: absolute; left: 0; top: 6px; width: 5px; height: 5px; background: var(--blue);
  }
  .setup .brand { margin-top: auto; gap: 8px; justify-content: center; }
  .setup .brand-dot { width: 20px; height: 20px; }
  .setup .brand-name { font-size: 24px; letter-spacing: 1px; }
</style>
</head>
<body>

  <section class="card front" aria-label="Postcard front">
    <header class="front-top">
      <div class="brand">
        <span class="brand-dot"></span>
        <span class="brand-name">789 Brookvale</span>
      </div>
    </header>
    <h1 class="headline">YOU'RE SPENDING TOO MUCH ON TAXES!</h1>
    <p class="tagline-box">That's what they'll say if your business doesn't have a <em>789 Brookvale Outlay Plan.</em></p>
    <h2 class="who">Who should have a 789 Brookvale Outlay Plan?</h2>
    <div class="points">
      <p class="point">Every business owner who is incorporated should have one.</p>
      <p class="point">Write off 100% of this QTB approved this method.</p>
      <p class="point">It is the most tax effective way to run dental, health, vision and other expenses through your company.</p>
      <p class="point">Easy to use APP for your phone, 2-day turnaround time for claims</p>
    </div>
    <div class="url-bar">www.789brookvale.com</div>
  </section>

  <section class="card back" aria-label="Postcard back">
    <div class="example">
      <p class="lead">Assuming a 38% personal tax rate. You will need to earn $1.62 of gross income, pay $0.62 of personal tax, which leaves you with $1.00 of after tax money to use for your personal expenses.</p>
      <p class="lead strong">The example of using a 789 Brookvale Outlay Plan, or doing nothing would need the following information :</p>
      <p class="sub">Comparison</p>
      <ul><li><span class="amt">$5,000</span> of medical, dental, vision expenses</li></ul>
      <p class="sub">Do Nothing 789 Brookvale Outlay Plan</p>
      <ul>
        <li><span class="amt">$8,100</span> – Total Cost &nbsp;<span class="amt">$5,525</span> – Total Cost</li>
        <li><span class="amt">$3,100</span> – Income Tax <span class="amt">$500</span> fee &amp; <span class="amt">$25</span> GST</li>
        <li><span class="amt">$5,000</span> – Money needed for medical, dental, vision, etc.</li>
        <li><span class="amt">$5,000</span> – Money needed for medical, dental, vision, etc.</li>
        <li class="plain">SAVINGS is <span class="amt">$2,575</span></li>
        <li>Assuming a company incorporated in Alberta and a one time setup fee of <span class="amt">$275</span> has not been included in the comparison.</li>
      </ul>
    </div>
    <div class="setup">
      <h3>Information to send us to setup your account is:</h3>
      <ul>
        <li>Names and birth dates of you and your dependents</li>
        <li>Contact information for you and your business (if different) &nbsp;Address, email, phone numbers</li>
        <li>We will contact you about how to setup the app, your banking details and some other items.</li>
        <li>Setup fee is a one-time payment of $275</li>
      </ul>
      <div class="brand">
        <span class="brand-dot"></span>
        <span class="brand-name">789 Brookvale</span>
      </div>
    </div>
  </section>

</body>
</html>
```